Zielgruppe
Wir sind ein Buchverlag für Kinderbücher. Zielgruppe bei diesem Projekt sind Jungs ab 5 bis 10 Jahren.
Aufgabenstellung
Das Cover sollte Verlagsniveau haben. Außerdem ist es mir wichtig, das der Hauptbuchtitel gut lesbar ist auch auf mobilen Geräten.
Auch unser Logo soll vorne mit auf das Cover. Natürlich professionell und passend eingefügt.
Das Bild wurde von unserem Illustrator erstellt
Klappentext für die Rückseite ist im Anhang. Der Buchtitel sollte auch oben auf die Rückseite.
Buchtitel: Kleiner Sternenfänger...ein echter Abenteurer im Wind!
Untertitel: Mutmachbuch für tolle Jungs. Motivierende Geschichten für mehr Selbstvertrauen, innere Stärke und Achtsamkeit.
In einem Kreis einfügen (oder ähnliches auf der Front): Mit Traumreisen zum Vorlesen und Anhören!
Autorin Henrike Maurbacher
Format für Vendora: 15.24 x 21.31 / 6 x 9
Seiten Taschenbuch: 143
Seiten Gebundene Ausgabe: 142
Datei wird benötigt für: E-book, Taschenbuch, Gebundene Ausgabe (bei Bedarf Vorlage Anfragen)
Vorgaben E-book: https://pub.vendora-beispiel.com/de_DE/help/topic/G200645690
Wenn es Fragen gibt, dann bitte einfach melden.

```html
<!DOCTYPE html>
<html lang="de">
<head>
<meta charset="utf-8">
<title>Kleiner Sternenfänger – Cover</title>
<link href="https://fonts.googleapis.com/css2?family=Fira+Sans+Extra+Condensed:wght@400;700&family=Lilita+One&family=Open+Sans:wght@400;600;700&display=swap" rel="stylesheet">
<style>
  :root {
    --stage: #f1f1f1;
    --leaf-light: #b4cf6e;
    --leaf-mid: #8fb84e;
    --leaf-deep: #5f9a3c;
    --trunk: #b5773a;
    --crown: #f3dc5a;
    --hair: #8a5a35;
    --skin: #efc39c;
    --shirt: #bfe0dc;
    --title-yellow: #f6e95a;
    --title-shadow: rgba(60, 80, 20, 0.55);
    --ink: #1f2a1a;
    --badge-blue: #5e94c8;
    --sky-blue: #3f79b8;
    --warm-orange: #eea63a;
    --warm-red: #e25b48;
    --paper: #ffffff;
    --text-light: #ffffff;
  }
  * { box-sizing: border-box; margin: 0; padding: 0; }
  html, body { width: 1200px; height: 1194px; overflow: hidden; }
  body { background: var(--stage); position: relative; font-family: "Open Sans", sans-serif; }

  .cover {
    position: absolute; top: 181px; width: 555px; height: 832px; overflow: hidden;
    box-shadow: 0 6px 18px rgba(0,0,0,0.15);
  }
  .cover--front { left: 30px; }
  .cover--back { left: 615px; }

  .cover__artwork {
    position: absolute; inset: 0;
    background:
      linear-gradient(100deg, transparent 62%, rgba(181,119,58,0.45) 66%, rgba(181,119,58,0.45) 72%, transparent 76%),
      radial-gradient(ellipse at 25% 20%, var(--leaf-deep) 0, transparent 55%),
      radial-gradient(ellipse at 85% 60%, var(--leaf-deep) 0, transparent 45%),
      linear-gradient(180deg, var(--leaf-mid) 0%, var(--leaf-light) 55%, var(--leaf-mid) 100%);
  }
  .front__hero {
    position: absolute; left: 90px; top: 285px; width: 360px; height: 547px;
    border-radius: 180px 180px 40px 40px;
    background: linear-gradient(180deg,
      var(--crown) 0%, var(--crown) 20%,
      var(--hair) 27%, var(--hair) 38%,
      var(--skin) 44%, var(--skin) 74%,
      var(--shirt) 80%, var(--paper) 88%, var(--shirt) 100%);
    opacity: 0.9;
  }
  .cover--back .cover__artwork {
    background:
      radial-gradient(ellipse at 20% 20%, var(--leaf-deep) 0, transparent 50%),
      radial-gradient(ellipse at 80% 95%, var(--leaf-deep) 0, transparent 40%),
      linear-gradient(180deg, var(--leaf-mid) 0%, var(--leaf-light) 60%, var(--leaf-mid) 100%);
  }

  .front__author {
    position: absolute; top: 22px; left: 0; right: 0; text-align: center;
    font-family: "Fira Sans Extra Condensed", sans-serif; font-size: 24px;
    color: var(--title-yellow); letter-spacing: 0.3px;
  }
  .front__title {
    position: absolute; top: 62px; left: 0; right: 0; text-align: center;
    font-family: "Fira Sans Extra Condensed", sans-serif; font-weight: 700;
    font-size: 56px; line-height: 1.08; color: var(--title-yellow);
    text-shadow: 0 2px 8px var(--title-shadow);
  }
  .front__badge {
    position: absolute; left: 430px; top: 555px; width: 108px; height: 108px;
    border-radius: 50%; background: var(--badge-blue); color: var(--text-light);
    display: flex; align-items: center; justify-content: center; text-align: center;
    font-size: 14px; line-height: 1.15; font-weight: 600; transform: rotate(6deg);
  }
  .front__subtitle {
    position: absolute; left: 92px; top: 705px; width: 420px;
    font-size: 14.5px; font-weight: 600; line-height: 1.3; color: var(--ink);
    transform: rotate(-2deg);
  }
  .publisher {
    position: absolute; display: flex; align-items: center; gap: 7px;
    font-family: "Open Sans", sans-serif; font-weight: 700; color: var(--ink);
    line-height: 1; text-transform: uppercase; letter-spacing: 0.5px;
  }
  .publisher__dot { width: 14px; height: 14px; border-radius: 50%; background: var(--ink); flex: none; }
  .publisher__name { font-size: 15px; line-height: 1.05; }
  .cover--front .publisher { left: 400px; top: 764px; }
  .cover--back .publisher { left: 385px; top: 712px; }

  .bubble {
    position: absolute; border-radius: 50%; display: flex; flex-direction: column;
    align-items: center; justify-content: center; text-align: center;
  }
  .bubble--title {
    left: 30px; top: 42px; width: 160px; height: 160px; background: var(--paper);
    font-family: "Lilita One", sans-serif; color: var(--sky-blue);
    font-size: 15px; line-height: 1.05; text-transform: uppercase; padding: 18px;
  }
  .bubble--promise {
    left: 215px; top: 70px; width: 245px; height: 245px; background: var(--paper);
    padding: 20px; font-weight: 600; line-height: 1.12;
  }
  .promise__lead { color: var(--badge-blue); font-size: 15px; margin-bottom: 6px; }
  .promise__main { color: var(--warm-red); font-size: 15px; margin-bottom: 6px; }
  .promise__extra { color: var(--warm-orange); font-size: 15px; }

  .bubble h3 { font-size: 13px; font-weight: 600; line-height: 1.2; margin-bottom: 6px; }
  .bubble p { font-size: 10px; line-height: 1.25; }
  .bubble--treasure {
    left: 22px; top: 268px; width: 236px; height: 236px; background: var(--warm-orange);
    color: var(--text-light); padding: 26px 30px;
  }
  .bubble--unique {
    left: 282px; top: 348px; width: 262px; height: 262px; background: var(--warm-red);
    color: var(--text-light); padding: 30px 34px;
  }
  .bubble--unique p { font-size: 9.5px; }
  .bubble--stories {
    left: 28px; top: 520px; width: 300px; height: 300px; background: var(--sky-blue);
    color: var(--text-light); padding: 30px 36px;
  }
  .bubble--stories h3 { font-size: 12.5px; }
  .bubble--stories p { font-size: 9.5px; }
</style>
</head>
<body>

<section class="cover cover--front">
  <div class="cover__artwork" role="img" aria-label="Illustration: Waldhintergrund mit Bäumen"></div>
  <div class="front__hero" role="img" aria-label="Illustration: Junge mit Brille, Krone und gestreiftem Shirt, daneben ein Specht am Baum"></div>
  <p class="front__author">Henrike Maurbacher</p>
  <h1 class="front__title">Kleiner Sternenfänger...<br>ein echter Abenteurer<br>im Wind!</h1>
  <div class="front__badge">Mit<br>Traumreisen<br>zum Vorlesen<br>und Anhören!</div>
  <p class="front__subtitle">Mutmachbuch für tolle Jungs. Motivierende Geschichten für mehr Selbstvertrauen, innere Stärke und Achtsamkeit.</p>
  <div class="publisher"><span class="publisher__dot"></span><span class="publisher__name">Heiterwind<br>Verlag</span></div>
</section>

<section class="cover cover--back">
  <div class="cover__artwork" role="img" aria-label="Illustration: Waldlandschaft mit Bäumen und Blättern"></div>

  <div class="bubble bubble--title">Kleiner Sternen&shy;fänger... ein echter Abenteurer im Wind!</div>

  <div class="bubble bubble--promise">
    <p class="promise__lead">Mutmachbuch<br>für tolle Jungs.</p>
    <p class="promise__main">Motivierende Geschichten für mehr Selbstvertrauen, innere Stärke und Achtsamkeit.</p>
    <p class="promise__extra">Mit Traumreisen zum Vorlesen und Anhören!</p>
  </div>

  <div class="bubble bubble--treasure">
    <h3>Du bist ein<br>Schatz! Weißt du das?</h3>
    <p>Ein Schatz ist etwas ganz Wertvolles. Wenn du einen Schatz hast, dann freust du dich darüber. Du passt gut auf ihn auf und er ist dir sehr wichtig, nicht wahr? So ein Schatz bist du auch! Warum? Einfach deswegen, weil du DU bist: ein toller Junge. Bitte vergiss das nie!</p>
  </div>

  <div class="bubble bubble--unique">
    <h3>Du bist<br>einzigartig.</h3>
    <p>Kein anderer Junge auf der ganzen Welt ist so wie du. Du bist so einmalig wie ein Fingerabdruck. So einmalig wie der größte Diamant. So einmalig wie eine Schneeflocke. Manchmal kommt es dir vielleicht so vor, als wärst du nichts Besonderes. Aber ich verspreche dir, du wirst entdecken, was alles in dir steckt: Mut und Selbstvertrauen und Kraft und Fröhlichkeit. Das alles hast du in dir!</p>
  </div>

  <div class="bubble bubble--stories">
    <h3>In diesem Buch findest du spannende, lustige Geschichten über Flynn, Mats und Tino, drei Jungs so wie du!</h3>
    <p>Was die drei lernen, kannst du auch lernen: An dich selbst zu glauben. Zu wissen, dass du wichtig bist. Dir und deinen Eltern zu vertrauen. Wenn du das gelernt hast, dann kannst du jede Herausforderung meistern und alle Probleme überwinden. Dann kannst du fröhlich und selbstbewusst und großartig sein. Ein echter Schatz!</p>
  </div>

  <div class="publisher"><span class="publisher__dot"></span><span class="publisher__name">Heiterwind<br>Verlag</span></div>
</section>

</body>
</html>
```